Luma Tostada - Neighborhood Mailer

We need a postcard design for a new catering business call 'Luma Tostada". We make affordable gourmet style healthy ceviches. This postcard should announce our catering business, as well as highlight the local farmer's markets where customer can find us and purchase individual already prepared ceviches. We would like the design to focus on eating healthy, eat fresh ingredients instead of hot and heavy meals here (in Houston, TX). The final design should look and feel refreshing, healthy and announce us as a new food alternative.

Target Market(s)

18-50 year olds, male or female, Healthy conscious individuals, businesses needing catering, fitness enthusiast, fresh ingredients,

Industry/Entity Type

Health And Wellness

Font styles to use
Sans Serif

Colors
33a6d7

Requirements
Must have
• Promote the ceviche a something fresh, something different and healthy to the Houston market. Must have our logo, website, and contact info on the front or back of the postcard.
Nice to have
• Would like lots of pictures of fresh ingredients, and limes

```html
<!DOCTYPE html>
<html lang="en">
<head>
<meta charset="utf-8">
<title>Luma Tostada – Neighborhood Mailer</title>
<link rel="stylesheet" href="https://fonts.googleapis.com/css2?family=Roboto+Condensed:wght@400;700&family=Open+Sans:wght@400;600;700&display=swap">
<style>
  :root{
    --blue:#33a6d7;
    --blue-deep:#1d86bd;
    --ink:#3a3f44;
    --grey:#8a9096;
    --paper:#ffffff;
    --backdrop:#e6e8ea;
  }
  *{box-sizing:border-box;margin:0;padding:0}
  html,body{width:674px;height:1200px;overflow:hidden;background:var(--backdrop)}
  body{position:relative;font-family:"Open Sans",sans-serif;color:var(--ink)}
  .card{position:absolute;left:34px;width:606px;background:var(--paper);overflow:hidden;box-shadow:0 3px 10px rgba(0,0,0,.18)}
  .front{top:20px;height:610px}
  .back{top:650px;height:520px}
  .abs{position:absolute}
  .cond{font-family:"Roboto Condensed",sans-serif}

  /* front */
  .hero-photo{left:0;top:0;width:606px;height:230px;
    background:radial-gradient(circle at 30% 45%,#f2d6cf 0,#e8a8a0 22%,#c9d8b4 45%,#8fb07a 62%,transparent 80%),
    linear-gradient(90deg,#e9e3da 0%,#d9c2b4 55%,#e9a25a 78%,#d7b98a 100%)}
  .band{left:0;top:0}
  .headline{left:0;width:606px;top:222px;text-align:center;color:#fff;font-weight:700;font-size:31px;letter-spacing:.5px}
  .subhead{left:0;width:606px;top:260px;text-align:center;color:#fff;font-weight:700;font-size:19px;letter-spacing:.6px}
  .market{top:298px;color:#fff;font-size:17px;line-height:1.25}
  .market.one{left:140px}
  .market.two{left:330px}
  .dish-photo{left:190px;top:340px;width:226px;height:130px;border-radius:6px;
    background:radial-gradient(ellipse at 50% 55%,#f0c9b8 0,#e59a86 30%,#b7cf9a 55%,#d9eef6 80%)}
  .catering{left:24px;top:500px;color:var(--blue);font-weight:700;font-size:21px;line-height:1.05}
  .catering small{display:block;color:var(--grey);font-weight:400;font-size:13px;margin-top:8px}
  .call{right:26px;top:505px;text-align:left;color:var(--ink)}
  .call .label{font-size:17px;letter-spacing:.4px}
  .call .phone{font-weight:700;font-size:25px;color:var(--blue-deep);line-height:1.1}
  .call .web{font-size:13px;color:var(--grey);margin-top:10px}
  .brand-badge{left:243px;top:470px;width:120px;height:120px;border-radius:50%;background:#fff;border:4px solid var(--blue);
    display:flex;align-items:center;justify-content:center;text-align:center}
  .brand-name{font-family:"Open Sans",sans-serif;font-weight:700;color:var(--blue);font-size:17px;line-height:1.1}

  /* back */
  .back-photo{left:0;top:0;width:606px;height:520px;
    background:radial-gradient(ellipse at 60% 45%,#f4f4f4 0,#e4e6e8 40%,#fbfbfb 75%)}
  .tagline{left:330px;top:48px;font-family:"Roboto Condensed",sans-serif;font-weight:700;line-height:1.05}
  .tagline .top{font-size:40px;color:var(--ink);padding-left:44px}
  .tagline .bottom{font-size:40px;color:var(--blue)}
  .back .brand-badge{left:70px;top:140px;width:170px;height:170px;border-width:5px}
  .back .brand-name{font-size:24px}
  .back-contact{left:28px;top:345px;color:#fff}
  .back-contact .label{font-size:22px;letter-spacing:.5px}
  .back-contact .phone{font-weight:700;font-size:38px;line-height:1.1}
  .back-contact .web{font-size:17px;margin-top:16px}
  .indicia{left:460px;top:222px;width:120px;height:54px;border:1px solid #b9bec3;font-size:8px;line-height:1.3;text-align:center;color:var(--grey);padding:6px 4px;text-transform:uppercase}
  .ecrwss{left:440px;top:300px;width:140px;border-bottom:1px solid #b9bec3;font-size:9px;color:var(--grey);padding-bottom:2px}
  .recipient{left:374px;top:384px;font-size:11px;line-height:1.4;color:var(--ink)}
</style>
</head>
<body>

<section class="card front" aria-label="Postcard front">
  <div class="abs hero-photo" role="img" aria-label="Photo of a bowl of fresh shrimp ceviche with tomato, onion and cilantro beside tortilla chips"></div>
  <svg class="abs band" width="606" height="610" viewBox="0 0 606 610" aria-hidden="true">
    <defs>
      <linearGradient id="bandGrad" x1="0" y1="0" x2="0" y2="1">
        <stop offset="0" stop-color="#2f9fd2"/>
        <stop offset="1" stop-color="#1d86bd"/>
      </linearGradient>
    </defs>
    <path d="M0 205 Q303 170 606 210 L606 212 Q303 176 0 210 Z" fill="#bfe3f2"/>
    <path d="M0 212 Q303 178 606 214 L606 360 Q303 330 0 360 Z" fill="url(#bandGrad)"/>
    <line x1="303" y1="296" x2="303" y2="336" stroke="#fff" stroke-width="1" opacity=".7"/>
  </svg>
  <h1 class="abs headline cond">HEALTHY FRESH INGREDIENTS</h1>
  <p class="abs subhead cond">COOL AND REFRESHING CEVICHE</p>
  <p class="abs market one">Elm Village Market<br>Aug. 8th &amp; 9th</p>
  <p class="abs market two">Town Square Farmer's Market<br>Sept. 9th</p>
  <div class="abs dish-photo" role="img" aria-label="Photo of a takeaway container filled with prepared ceviche"></div>
  <p class="abs catering cond">CATERING AVAILABLE<br>FOR EVERYDAY<small>OR SPECIAL OCCASIONS</small></p>
  <div class="abs brand-badge"><span class="brand-name">Luma<br>Tostada</span></div>
  <div class="abs call">
    <p class="label cond">CALL US TODAY</p>
    <p class="phone cond">(855)-4-TOSTADA</p>
    <p class="web">www.lumatostada.com</p>
  </div>
</section>

<section class="card back" aria-label="Postcard back">
  <div class="abs back-photo" role="img" aria-label="Faint photo of fresh ceviche ingredients"></div>
  <svg class="abs" style="left:0;top:0" width="606" height="520" viewBox="0 0 606 520" aria-hidden="true">
    <path d="M0 330 L250 330 A90 90 0 0 0 330 250 L330 520 L0 520 Z" fill="var(--blue-deep)"/>
    <path d="M0 340 L330 340 L330 520 L0 520 Z" fill="var(--blue)"/>
    <path d="M250 225 A95 95 0 0 1 155 320" fill="none" stroke="var(--blue)" stroke-width="3"/>
  </svg>
  <h2 class="abs tagline"><span class="top" style="display:block">MORE THAN</span><span class="bottom" style="display:block">AN APPETIZER</span></h2>
  <div class="abs brand-badge"><span class="brand-name">Luma<br>Tostada</span></div>
  <div class="abs back-contact">
    <p class="label cond">CALL US TODAY</p>
    <p class="phone cond">(855)-4-TOSTADA</p>
    <p class="web">www.lumatostada.com</p>
  </div>
  <div class="abs indicia">Presorted Standard<br>U.S. Postage Paid<br>Tostada, LLC</div>
  <p class="abs ecrwss">ECRWSS</p>
  <p class="abs recipient">Local<br>Postal Customer</p>
</section>

</body>
</html>
```